Tilwa Sandrim Construction
Business Cards, Note Pads, Envelopes, Letterhead , signboard etc.
Bright & Fun-filled
Hamdan R. Al-Qutami
CEO
P.O Box 40573
Al-Hassa 36417
Saudi Arabia
Hamdan@tilwasandrim.com.sa
www.tilwasandrim.com.sa
Leave the back of the business card to write all the information in arabic
similar logo

```html
<!DOCTYPE html>
<html lang="en">
<head>
<meta charset="utf-8">
<title>Tilwa Sandrim Construction – Business Card</title>
<link href="https://fonts.googleapis.com/css2?family=Ubuntu:wght@400;500;700&display=swap" rel="stylesheet">
<style>
  :root {
    --backdrop: #ece7df;
    --card: #ffffff;
    --brand-red: #c8161d;
    --brand-red-dark: #a80f15;
    --ink: #3a3a3a;
    --band-grey: #c4c4c6;
  }
  * { margin: 0; padding: 0; box-sizing: border-box; }
  html, body {
    width: 1200px; height: 965px; overflow: hidden;
    background: var(--backdrop);
    font-family: "Ubuntu", Arial, sans-serif;
  }
  .business-card {
    position: absolute; left: 150px; top: 197px;
    width: 900px; height: 570px;
    background: var(--card);
    border-radius: 34px;
    overflow: hidden;
    box-shadow: 0 10px 30px rgba(0,0,0,0.18);
  }
  .brand {
    position: absolute; left: 70px; top: 200px; width: 380px;
    display: flex; align-items: center; gap: 20px;
  }
  .brand-dot {
    width: 56px; height: 56px; border-radius: 50%;
    background: var(--brand-red); flex: none;
  }
  .brand-name {
    color: var(--brand-red); font-weight: 700;
    font-size: 38px; line-height: 1.1; text-transform: uppercase;
  }
  .contact-block { position: absolute; left: 531px; top: 44px; color: var(--ink); }
  .person-name { color: var(--brand-red); font-weight: 500; font-size: 34px; line-height: 40px; }
  .person-role { font-size: 24px; margin-top: 6px; }
  .address { font-size: 22px; line-height: 40px; margin-top: 40px; }
  .contact-list { list-style: none; margin-top: 22px; }
  .contact-list li {
    display: flex; align-items: center; gap: 14px;
    font-size: 22px; line-height: 40px;
  }
  .contact-list svg { width: 21px; height: 21px; fill: var(--brand-red); flex: none; }
  .footer-band {
    position: absolute; left: 0; bottom: 0; width: 900px; height: 92px;
    background: linear-gradient(to bottom, var(--band-grey) 0%, var(--band-grey) 14%, var(--brand-red) 14%, var(--brand-red-dark) 100%);
  }
</style>
</head>
<body>
  <div class="business-card">
    <div class="brand">
      <span class="brand-dot"></span>
      <span class="brand-name">Tilwa Sandrim<br>Construction</span>
    </div>

    <div class="contact-block">
      <div class="person-name">Hamdan R. Al-Qutami</div>
      <div class="person-role">CEO</div>
      <div class="address">P.O Box 40573,<br>Al-Hassa 36417, Saudi Arabia</div>
      <ul class="contact-list">
        <li><svg viewBox="0 0 24 24"><path d="M6.6 10.8a15 15 0 0 0 6.6 6.6l2.2-2.2c.3-.3.7-.4 1-.2 1.1.4 2.3.6 3.6.6.6 0 1 .4 1 1V20c0 .6-.4 1-1 1C10.6 21 3 13.4 3 4c0-.6.4-1 1-1h3.5c.6 0 1 .4 1 1 0 1.3.2 2.5.6 3.6.1.3 0 .7-.2 1z"/></svg>+96635218470</li>
        <li><svg viewBox="0 0 24 24"><path d="M8 1h8a2 2 0 0 1 2 2v18a2 2 0 0 1-2 2H8a2 2 0 0 1-2-2V3a2 2 0 0 1 2-2zm0 3v14h8V4zm4 15.5a1 1 0 1 0 0 2 1 1 0 0 0 0-2z"/></svg>+966507362915</li>
        <li><svg viewBox="0 0 24 24"><path d="M6 2h10v5H6zM3 8h18v8h-3v6H6v-6H3zm5 6v6h8v-6z"/></svg>+96635218471</li>
        <li><svg viewBox="0 0 24 24"><path d="M12 2a10 10 0 1 0 5 18.7l-1-1.7A8 8 0 1 1 20 12v1a2 2 0 0 1-4 0V7h-2v1a5 5 0 1 0 .8 6.8A4 4 0 0 0 22 13v-1A10 10 0 0 0 12 2zm0 13a3 3 0 1 1 0-6 3 3 0 0 1 0 6z"/></svg>Hamdan@tilwasandrim.com.sa</li>
        <li><svg viewBox="0 0 24 24"><path d="M12 2a10 10 0 1 0 0 20 10 10 0 0 0 0-20zm6.9 6h-3a15 15 0 0 0-1.4-3.9A8 8 0 0 1 18.9 8zM12 4c.8 1.2 1.5 2.5 1.9 4h-3.8c.4-1.5 1.1-2.8 1.9-4zM4.3 14a8 8 0 0 1 0-4h3.4a16 16 0 0 0 0 4zm.8 2h3a15 15 0 0 0 1.4 3.9A8 8 0 0 1 5.1 16zm3-8h-3a8 8 0 0 1 4.4-3.9C9 5.2 8.5 6.6 8.1 8zM12 20c-.8-1.2-1.5-2.5-1.9-4h3.8c-.4 1.5-1.1 2.8-1.9 4zm2.3-6H9.7a14 14 0 0 1 0-4h4.6a14 14 0 0 1 0 4zm.2 5.9a15 15 0 0 0 1.4-3.9h3a8 8 0 0 1-4.4 3.9zm1.8-5.9a16 16 0 0 0 0-4h3.4a8 8 0 0 1 0 4z"/></svg>www.tilwasandrim.com.sa</li>
      </ul>
    </div>

    <div class="footer-band" role="img" aria-label="Decorative grey and red wave band along the bottom edge"></div>
  </div>
</body>
</html>
```